Business Cards - New Logo Rebranding

Hello We know have a red and blue logo and are looking to create new cards. We are looking for the best creativity of the new logo merged with some of the existing artwork provided.

Target Market(s)

Realtors

Industry/Entity Type

Real Estate

Contact Information for Business Card

New logo with rebranded colors

Requirements
Must have
• Creative use of the new logo

```html
<!DOCTYPE html>
<html lang="en">
<head>
<meta charset="utf-8">
<title>Summit Crest Business Card</title>
<link href="https://fonts.googleapis.com/css2?family=Exo+2:wght@700;800&family=Lato:wght@400&family=Montserrat:wght@500;700&family=Aldrich&display=swap" rel="stylesheet">
<style>
  :root{
    --stage:#2b2b2b;
    --brand-blue:#1573bd;
    --deep-blue:#1a5fa8;
    --brand-red:#e63b3f;
    --white:#ffffff;
    --silver:#c9ccd1;
    --text-blue:#1d5aa6;
  }
  *{margin:0;padding:0;box-sizing:border-box}
  html,body{width:1200px;height:1000px;overflow:hidden;background:var(--stage)}
  .card{position:absolute;left:202px;width:796px;height:455px;border-radius:20px;overflow:hidden}
  .card-front{top:35px;background:var(--brand-blue)}
  .card-back{top:511px;background:var(--white)}

  .brand{position:absolute;text-align:center}
  .brand-mark{display:block;margin:0 auto;border-radius:50%;background:var(--silver);border:6px solid var(--brand-red)}
  .brand-name{font-family:"Exo 2",sans-serif;font-weight:800;letter-spacing:2px;line-height:1}
  .brand-tagline{font-family:"Montserrat",sans-serif;font-weight:700;font-size:10px;letter-spacing:.3px;margin-top:6px}

  .front-brand{left:55px;top:108px;width:290px}
  .front-brand .brand-mark{width:146px;height:146px}
  .front-brand .brand-name{color:var(--white);font-size:32px;margin-top:10px}
  .front-brand .brand-tagline{color:var(--white)}

  .person{position:absolute;left:383px;top:102px;color:var(--white);font-family:"Exo 2",sans-serif;font-weight:800}
  .person-name{font-size:31px;letter-spacing:1.5px}
  .person-title{font-size:19px;letter-spacing:.8px;margin-top:6px}
  .person-rule{width:126px;height:2px;background:var(--white);margin-top:18px}

  .contacts{position:absolute;left:383px;top:208px;list-style:none;font-family:"Lato",sans-serif;font-size:20px;color:var(--white)}
  .contacts li{display:flex;align-items:center;height:32px}
  .contact-icon{width:22px;height:22px;background:var(--brand-red);border-radius:3px;margin-right:10px;display:flex;align-items:center;justify-content:center}

  .services{position:absolute;left:0;right:0;top:392px;text-align:center;font-family:"Exo 2",sans-serif;font-weight:800;font-size:20px;letter-spacing:.8px;color:var(--white)}
  .services .dot{display:inline-block;width:8px;height:8px;border-radius:50%;background:var(--brand-red);margin:0 6px 3px}

  .back-header{position:absolute;left:0;right:0;top:0;height:81px;background:var(--brand-blue);text-align:center;color:var(--white);font-family:"Montserrat",sans-serif}
  .back-kicker{font-weight:500;font-size:17px;padding-top:16px}
  .back-headline{font-weight:700;font-size:23px;margin-top:3px}

  .back-brand{left:50px;top:115px;width:280px}
  .back-brand .brand-mark{width:114px;height:114px;border-width:5px}
  .back-brand .brand-name{color:var(--deep-blue);font-size:24px;margin-top:8px}
  .back-brand .brand-tagline{color:var(--deep-blue);font-size:9px;margin-top:4px}

  .badges{position:absolute;left:38px;top:296px;width:300px}
  .badge{position:absolute}
  .badge-round{width:58px;height:58px;border-radius:50%}

  .reasons{position:absolute;left:353px;top:95px;width:430px;list-style:none;font-family:"Aldrich",sans-serif;font-size:19.5px;color:var(--text-blue);line-height:25px}
  .reasons li{position:relative;padding-left:38px;margin-bottom:7px}
  .reasons li::before{content:"";position:absolute;left:2px;top:50%;width:24px;height:24px;margin-top:-12px;border-radius:50%;background:var(--silver);border:3px solid var(--brand-red)}

  .back-stripe{position:absolute;left:0;right:0;bottom:0;height:11px}
</style>
</head>
<body>

<section class="card card-front">
  <div class="brand front-brand">
    <span class="brand-mark"></span>
    <div class="brand-name">SUMMIT CREST</div>
    <div class="brand-tagline">INSPECTION PROFESSIONALS</div>
  </div>

  <div class="person">
    <div class="person-name">DANA WHITMORE</div>
    <div class="person-title">CERTIFIED MOLD INSPECTOR</div>
    <div class="person-rule"></div>
  </div>

  <ul class="contacts">
    <li><span class="contact-icon"><svg width="14" height="14" viewBox="0 0 14 14"><rect x="1" y="1" width="12" height="12" rx="2" fill="none" stroke="#fff" stroke-width="1.6"/><rect x="4" y="3.5" width="3" height="7" fill="#fff"/><rect x="8.5" y="4" width="2.5" height="1.5" fill="#fff"/><rect x="8.5" y="7" width="2.5" height="1.5" fill="#fff"/></svg></span>800 555 0142</li>
    <li><span class="contact-icon"><svg width="14" height="14" viewBox="0 0 24 24"><path fill="#fff" d="M6.6 10.8a15.1 15.1 0 0 0 6.6 6.6l2.2-2.2a1 1 0 0 1 1-.25 11.4 11.4 0 0 0 3.6.57 1 1 0 0 1 1 1V20a1 1 0 0 1-1 1A17 17 0 0 1 3 4a1 1 0 0 1 1-1h3.5a1 1 0 0 1 1 1c0 1.25.2 2.45.57 3.6a1 1 0 0 1-.25 1z"/></svg></span>562 555 0187</li>
    <li><span class="contact-icon"><svg width="14" height="14" viewBox="0 0 24 24"><path fill="#fff" d="M2 11 22 3l-6 18-4-7zM12 14l6-8-8 6z"/></svg></span>dana.whitmore@summitcrestinspect.com</li>
    <li><span class="contact-icon"><svg width="14" height="14" viewBox="0 0 24 24"><circle cx="12" cy="12" r="9" fill="none" stroke="#fff" stroke-width="2.2"/><path d="M3 12h18M12 3c3 3 3 15 0 18M12 3c-3 3-3 15 0 18" fill="none" stroke="#fff" stroke-width="1.8"/></svg></span>www.summitcrestinspect.com</li>
  </ul>

  <div class="services">HOME<span class="dot"></span>SEWER<span class="dot"></span>MOLD<span class="dot"></span>COMMERCIAL<span class="dot"></span>TERMITE<span class="dot"></span>ROOF</div>
</section>

<section class="card card-back">
  <header class="back-header">
    <div class="back-kicker">CALIFORNIA'S #1 INSPECTION COMPANY!</div>
    <div class="back-headline">WHY CHOOSE THE SUMMIT CREST...</div>
  </header>

  <div class="brand back-brand">
    <span class="brand-mark"></span>
    <div class="brand-name">SUMMIT CREST</div>
    <div class="brand-tagline">INSPECTION PROFESSIONALS</div>
  </div>

  <div class="badges" aria-label="Certification and listing badges">
    <span class="badge badge-round" style="left:20px;top:0;background:#b8282e"></span>
    <span class="badge badge-round" style="left:100px;top:0;background:#c9a53a"></span>
    <span class="badge badge-round" style="left:180px;top:0;background:#a9acb1"></span>
    <span class="badge" style="left:0;top:72px;width:106px;height:44px;border-radius:22px 6px 6px 22px;background:#2b3a78"></span>
    <span class="badge" style="left:128px;top:72px;width:70px;height:44px;border-radius:4px;background:#d4262e"></span>
    <span class="badge badge-round" style="left:218px;top:74px;width:36px;height:36px;background:#8a5fc6"></span>
  </div>

  <ul class="reasons">
    <li>Performing Inspection Since 1984</li>
    <li>HomeCert Guild Certified Master / Professional Inspectors</li>
    <li>500,000+ Inspection Completed Statewide</li>
    <li>Request of Repairs Pricer Report</li>
    <li>90-Days Inspection Guarantees</li>
    <li>Aero-Board Drone Licensed Roof Inspectors upon request</li>
    <li>5,000+ 5 Star Reviews on ReviewHub &amp; StarList</li>
  </ul>

  <svg class="back-stripe" viewBox="0 0 796 11" preserveAspectRatio="none">
    <rect width="796" height="11" fill="#1573bd"/>
    <polygon points="498,0 796,0 796,11 486,11" fill="#e63b3f"/>
    <polygon points="490,0 498,0 486,11 478,11" fill="#ffffff"/>
  </svg>
</section>

</body>
</html>
```